Business Cards for a company that provides webstore services to veterinarians

We need business cards designed for our main service PawCartHub. PawCartHub is a webstore that veterinarian clinics can use to that will allow their clients to purchase products for their pets. Our company is Brindlow Veterinary Solutions (BVS). Our mission statement is We love pets! We will do everything possible to facilitate along, healthy and happy relationship with their families.

Target Market(s)

Veterinarians

Industry/Entity Type

Veterinary

Contact Information for Business Card

I would like the design to incorporate the colours our our company. Cards should have room for employee name, title (only necessary in two instances), phone number, mobile number, email address and linkedin symbol and related profile name ie Marla Quinton. I would like the PawCartHub logo to appear on one side and BVS logo to appear on the other. I will need both an english and french version. I can provide the french translation. Please focus on english version and then we will translate

Colors

Designer to choose colors to be used in the design.

Requirements
Must have
• one side - PawCartHub logo with persons name, phone number, mobile number, email address
• second side - BVS logo
• colours should be consistent with our company. colours are as follows:
• Red
• RGB: 190 / 30 / 45
• CYMK: 14 / 100 / 90 /10
• Hex: #BE1E2D
• Gray
• RGB: 88 / 89 / 86
• CYMK: 3 / 2 / 0 /64
• Hex: #585956
Nice to have
• address of company - can be on either side address is 4817 Feldmoor Street Suite 305 Burlington ON K2R 6T4. Toll free number will vary depending on person
• Linkedin symbol and name of person
• on second side with BVS logo our company's mission statement
Should not have
• nothing comes to mind

```html
<!DOCTYPE html>
<html lang="en">
<head>
<meta charset="utf-8">
<title>PawCartHub – Business Card</title>
<link rel="stylesheet" href="https://fonts.googleapis.com/css2?family=Montserrat:wght@400;600&family=Open+Sans:wght@600&display=swap">
<style>
  :root {
    --red: #BE1E2D;
    --gray: #585956;
    --card: #fbfbfa;
    --stage: #e8e6e3;
    --white: #ffffff;
    --profile-blue: #2a86c6;
  }
  * { box-sizing: border-box; margin: 0; padding: 0; }
  html, body {
    width: 1200px; height: 447px; overflow: hidden;
    background: var(--stage);
  }
  .canvas { position: relative; width: 1200px; height: 447px; }
  .card {
    position: absolute; top: 88px; width: 496px; height: 284px;
    background: var(--card);
    box-shadow: 0 2px 8px rgba(0,0,0,.18);
    font-family: "Montserrat", sans-serif;
    color: var(--gray);
    overflow: hidden;
  }
  .card--front { left: 78px; }
  .card--back { left: 609px; }

  .name-band {
    position: absolute; left: 0; top: 30px; width: 256px; height: 33px;
    background: var(--red); color: var(--white);
    border-radius: 0 10px 10px 0;
    box-shadow: 0 4px 5px rgba(0,0,0,.22);
    display: flex; align-items: center; padding-left: 27px;
    font-size: 15px; white-space: nowrap;
  }
  .name-band .title { font-size: 11.5px; margin-left: 4px; letter-spacing: .4px; }

  .brand-name {
    position: absolute; left: 0; right: 0; top: 128px;
    text-align: center;
    font-size: 48px; font-weight: 400; color: var(--gray);
    letter-spacing: -.5px; line-height: 1;
  }

  .contact {
    position: absolute; left: 0; right: 0; top: 222px;
    text-align: center; font-size: 13.5px; line-height: 22px; white-space: nowrap;
  }
  .contact .label { color: var(--red); font-weight: 600; }
  .contact .web { font-weight: 600; }
  .profile { display: inline-flex; align-items: center; gap: 4px; margin-left: 9px; font-size: 12px; }
  .profile .dot {
    width: 13px; height: 13px; border-radius: 50%; background: var(--profile-blue); display: inline-block;
  }

  .company-mark {
    position: absolute; left: 34px; top: 150px;
    display: flex; align-items: flex-start; gap: 9px;
  }
  .company-mark .circle {
    width: 12px; height: 12px; margin-top: 6px;
    border-radius: 50%; background: var(--red); flex: none;
  }
  .company-mark .name {
    font-size: 20px; font-weight: 400; color: var(--red); line-height: 24px;
  }

  .address {
    position: absolute; right: 35px; top: 182px;
    text-align: right; font-size: 13px; line-height: 17px; color: var(--gray);
    font-style: normal; white-space: nowrap;
  }
  .tag-band {
    position: absolute; right: 0; top: 222px; width: 227px; height: 34px;
    background: var(--red); color: var(--white);
    border-radius: 10px 0 0 10px;
    box-shadow: 0 4px 5px rgba(0,0,0,.22);
    display: flex; align-items: center; padding-left: 23px;
    font-family: "Open Sans", sans-serif; font-weight: 600; font-size: 16px; white-space: nowrap;
  }
</style>
</head>
<body>
<main class="canvas">
  <section class="card card--front" aria-label="Front of business card">
    <div class="name-band">YOUR NAME HERE,<span class="title">DIRECTOR</span></div>
    <div class="brand-name">PawCartHub</div>
    <div class="contact">
      <p><span class="label">T:</span> 012.555.0147, <span class="label">M:</span> 012.555.0147, <span class="label">E:</span> info@pawcarthub.com</p>
      <p><span class="web">www.pawcarthub.com</span><span class="profile"><span class="dot"></span>/Person name</span></p>
    </div>
  </section>

  <section class="card card--back" aria-label="Back of business card">
    <div class="company-mark">
      <span class="circle"></span>
      <span class="name">Brindlow<br>Veterinary<br>Solutions</span>
    </div>
    <address class="address">
      4817 Feldmoor Street Suite 305,<br>Burlington ON K2R 6T4
    </address>
    <div class="tag-band">business tag line here</div>
  </section>
</main>
</body>
</html>
```